'Vessel types, Demand, Supply & Disruptions - what's currently driving the bulk shipping

This is required for a talk that needs to cover the following matters

the difference between small, handysize, handymax, panamax, capesize, and very large bulk carriers, how the trade differs, self loading/unloading etc as an intro to the dry bulk trade and what's currently driving the bulk shipping markets.

The below is an initial breakdown on the slides but not finalised

There will need to be an additional slide on the importance of China for the dry bulk trades

Slide 1: Introduction

Welcome and brief overview of dry bulk shipping
Importance in global trade and economy
Slide 2: Types of Dry Bulk Vessels

Capesize: 100,000-400,000 DWT
Panamax: 60,000-100,000 DWT
Supramax: 45,000-60,000 DWT
Handysize: 15,000-45,000 DWT
Description and key features of each vessel type
Slide 3: Vessel Characteristics

Holds and hatches
Draft, beam, and length
Cargo handling equipment
Engine types and power
Slide 4: Routing in Dry Bulk Shipping

Major shipping routes (e.g., Cape of Good Hope, Panama Canal)
Factors influencing routing decisions (e.g., weather, fuel costs)
Strategic chokepoints and canals
Slide 5: Fixing and Chartering

Voyage Charter
Owner's responsibility
Charterer's responsibility
Time Charter
Bareboat Charter
Spot and long-term contracts
Slide 6: Key Charter Party (CP) Terms

Laytime and demurrage
Freight rates
Notice of Readiness (NOR)
Cargo quantities and quality
Ballast bonus
Slide 7: Current Disruptions in Dry Bulk Shipping

Impact of geopolitical events (e.g., trade tensions, conflicts) on shipping lanes
Effects of economic downturns (e.g., COVID-19 pandemic) on demand and supply chains
Environmental regulations affecting vessel operations
Port congestion and delays
Slide 8: Market Trends and Innovations

Technological advancements in vessel design (e.g., eco-friendly propulsion systems, fuel efficiency)
Digitalization and smart shipping solutions
Sustainability initiatives in the industry (e.g., ballast water treatment, emissions reduction)
Slide 9: Mitigation Strategies for Disruptions

Diversification of trading routes and markets
Investment in fleet optimization and efficiency measures
Collaboration with industry partners and stakeholders to address common challenges
Continuous monitoring and adaptation to changing market conditions
Slide 10: Case Study

Example of a recent disruption and its impact on dry bulk shipping operations
Lessons learned and strategies employed to mitigate the effects
Slide 11: Future Outlook

Anticipated trends and challenges in the dry bulk shipping industry
Opportunities for innovation and growth
Importance of sustainability and resilience in shaping the future of the industry
Slide 12: Conclusion

Recap of key points
Call to action for stakeholders to collaborate and innovate for a sustainable and resilient dry bulk shipping industry
Slide 13: Q&A

```html
<!DOCTYPE html>
<html lang="en">
<head>
<meta charset="utf-8">
<title>Bulk Shipping – Presentation Slides</title>
<link href="https://fonts.googleapis.com/css2?family=Barlow+Semi+Condensed:wght@600;700&family=Dosis:wght@400;500&family=Poppins:wght@400&display=swap" rel="stylesheet">
<style>
  :root{
    --ink:#1c1c1c;
    --accent:#1a8cf0;
    --muted:#555;
    --paper:#ffffff;
    --sea-deep:#0f5a8c;
    --sea-mid:#1c84b8;
    --sea-light:#3fa6d0;
    --art-light:#e4e6ea;
    --art-warm:#d98a7e;
  }
  *{margin:0;padding:0;box-sizing:border-box}
  html,body{width:1200px;height:1101px;overflow:hidden;background:var(--paper)}
  body{position:relative;font-family:'Poppins',sans-serif;color:var(--ink)}

  .slide{position:absolute;width:514px;height:289px;background:var(--paper);
    box-shadow:0 6px 22px rgba(0,0,0,.12);overflow:hidden}
  .col-a{left:71px}.col-b{left:623px}
  .row-1{top:64px}.row-2{top:397px}.row-3{top:733px}

  .heading{font-family:'Barlow Semi Condensed',sans-serif;font-weight:700}

  /* cover */
  .cover-bg{position:absolute;inset:0;
    background:radial-gradient(ellipse at 50% 60%,var(--sea-light) 0%,var(--sea-mid) 45%,var(--sea-deep) 100%)}
  .cover-ship{position:absolute;left:76px;top:161px;width:363px;height:72px;border-radius:4px;
    background:linear-gradient(90deg,#d8d6cf 0%,#b8786c 35%,#6f86b0 65%,#c9c7bf 100%);opacity:.85}
  .cover-title{position:absolute;top:34px;width:100%;text-align:center;font-size:29px;line-height:32px;color:#fff;letter-spacing:.5px}
  .cover-box{position:absolute;left:32px;top:85px;width:449px;height:59px;border:1px solid rgba(255,255,255,.45);
    border-radius:6px;text-align:center;color:#fff}
  .cover-box h2{font-size:20px;line-height:22px;margin-top:8px}
  .cover-box p{font-family:'Barlow Semi Condensed',sans-serif;font-weight:600;font-size:12px;line-height:14px;margin-top:4px}
  .contacts{position:absolute;top:257px;left:60px;right:56px;display:flex;justify-content:space-between;
    font-family:'Dosis',sans-serif;font-size:10.5px;color:#fff;font-weight:500}
  .contacts span{display:flex;align-items:center;gap:6px}
  .dot-icon{width:15px;height:15px;border-radius:50%;background:#111;display:flex;align-items:center;justify-content:center}

  /* slide chrome */
  .brand{position:absolute;top:6px;right:5px;font-size:12.5px;line-height:14px}
  .brand b,.slide-title b{color:var(--accent);font-weight:700}
  .slide-title{position:absolute;top:26px;width:100%;text-align:center;font-size:17px;line-height:20px}
  .title-rule{position:absolute;top:54px;left:50%;width:31px;height:2px;margin-left:-15px;background:var(--accent)}
  .footer{position:absolute;bottom:6px;left:6px;right:6px;height:17px;display:flex;align-items:center;font-size:6.5px}
  .footer .url{display:flex;align-items:center;gap:5px}
  .footer .copy{position:absolute;left:50%;transform:translateX(-50%)}
  .footer .page{margin-left:auto;display:flex;align-items:center;gap:1px}
  .footer .page i{font-style:normal;background:var(--accent);color:#fff;padding:0 1px}
  .globe{width:17px;height:17px;border-radius:50%;background:#111;display:flex;align-items:center;justify-content:center}

  /* vessel columns */
  .vessel{position:absolute;width:120px;margin-left:-60px;text-align:center}
  .vessel-art{margin:0 auto;border-radius:3px;
    background:linear-gradient(135deg,var(--art-light) 0%,var(--art-warm) 100%)}
  .vessel h3{font-family:'Dosis',sans-serif;font-weight:500;font-size:14px;line-height:16px}
  .vessel .range{font-family:'Dosis',sans-serif;font-size:9.5px;line-height:11px;margin-top:2px}
  .vessel .unit{font-size:5.5px;line-height:8px;margin-top:2px}
  .vessel p{width:80px;margin:4px auto 0;font-size:5.2px;line-height:9.3px;color:var(--muted)}

  .char{top:77px}
  .char .vessel-art{height:54px}
  .char .label{height:30px;margin-top:19px;display:flex;align-items:center;justify-content:center}
  .char h3{font-size:11px;line-height:12.5px}
  .char p{margin-top:6px}

  .photo{position:absolute;border-radius:3px}
  .bullets{position:absolute;list-style:none;font-family:'Dosis',sans-serif;font-size:11.5px}
  .bullets li{position:relative;padding-left:11px}
  .bullets li::before{content:"";position:absolute;left:0;top:7px;width:4px;height:4px;border-radius:50%;background:var(--accent)}
</style>
</head>
<body>

<svg width="0" height="0" style="position:absolute">
  <symbol id="i-globe" viewBox="0 0 16 16"><g fill="none" stroke="#4aa3ff" stroke-width="1.2"><circle cx="8" cy="8" r="6"/><ellipse cx="8" cy="8" rx="2.6" ry="6"/><path d="M2 8h12M3 5h10M3 11h10"/></g></symbol>
  <symbol id="i-mail" viewBox="0 0 16 16"><rect x="3" y="4.5" width="10" height="7" rx="1" fill="#4aa3ff"/><path d="M3.5 5l4.5 3.5L12.5 5" fill="none" stroke="#111" stroke-width="1"/></symbol>
  <symbol id="i-phone" viewBox="0 0 16 16"><path d="M5 3l2 2.5-1.2 1.3a7 7 0 003.4 3.4L10.5 9 13 11l-1.3 1.8C7.5 12.5 3.5 8.5 3.2 4.3z" fill="#4aa3ff"/></symbol>
</svg>

<!-- Slide 1: cover -->
<section class="slide col-a row-1">
  <div class="cover-bg" role="img" aria-label="Aerial photo of deep blue sea"></div>
  <div class="cover-ship" role="img" aria-label="Aerial photo of a loaded container ship"></div>
  <h1 class="cover-title heading">BULK SHIPPING</h1>
  <div class="cover-box">
    <h2 class="heading">Vessel types, Demand, Supply &amp; Disruptions</h2>
    <p>- what's currently driving the bulk shipping?</p>
  </div>
  <div class="contacts">
    <span><i class="dot-icon"><svg width="11" height="11"><use href="#i-globe"/></svg></i>www.bulkdeckbriefing.com</span>
    <span><i class="dot-icon"><svg width="11" height="11"><use href="#i-mail"/></svg></i>hello@bulkdeckbriefing.com</span>
    <span><i class="dot-icon"><svg width="11" height="11"><use href="#i-phone"/></svg></i>+1 555 014 2290</span>
  </div>
</section>

<!-- Slide 2: vessel types -->
<section class="slide col-b row-1">
  <div class="brand heading">BULK <b>SHIPPING</b></div>
  <h2 class="slide-title heading">Types of <b>Dry Bulk Vessels</b></h2>
  <div class="title-rule"></div>
  <div class="vessel" style="left:64px;top:83px">
    <div class="vessel-art" style="width:56px;height:52px" role="img" aria-label="Capesize bulk carrier picture"></div>
    <h3 style="margin-top:6px">Capesize</h3><div class="range">100,000-400,000</div><div class="unit">DWT</div>
    <p>Omnis isasdte natus errorsit voluseptatem accusantium doloremque laudantium, totasem rsem.</p></div>
  <div class="vessel" style="left:186px;top:83px">
    <div class="vessel-art" style="width:86px;height:52px" role="img" aria-label="Panamax bulk carrier picture"></div>
    <h3 style="margin-top:6px">Panamax</h3><div class="range">60,000-100,000</div><div class="unit">DWT</div>
    <p>Omnis isasdte natus errorsit voluseptatem accusantium doloremque laudantium, totasem rsem.</p></div>
  <div class="vessel" style="left:317px;top:83px">
    <div class="vessel-art" style="width:94px;height:52px" role="img" aria-label="Supramax bulk carrier picture"></div>
    <h3 style="margin-top:6px">Supramax</h3><div class="range">45,000-60,000</div><div class="unit">DWT</div>
    <p>Omnis isasdte natus errorsit voluseptatem accusantium doloremque laudantium, totasem rsem.</p></div>
  <div class="vessel" style="left:444px;top:83px">
    <div class="vessel-art" style="width:78px;height:52px" role="img" aria-label="Handysize bulk carrier picture"></div>
    <h3 style="margin-top:6px">Handysize</h3><div class="range">15,000-45,000</div><div class="unit">DWT</div>
    <p>Omnis isasdte natus errorsit voluseptatem accusantium doloremque laudantium, totasem rsem.</p></div>
  <div class="footer"><span class="url"><i class="globe"><svg width="12" height="12"><use href="#i-globe"/></svg></i>www.bulkdeckbriefing.com</span>
    <span class="copy">© 2024. ALL Rights Reserved.</span><span class="page">Page<i>02</i></span></div>
</section>

<!-- Slide 3: characteristics -->
<section class="slide col-a row-2">
  <div class="brand heading">BULK <b>SHIPPING</b></div>
  <h2 class="slide-title heading">Vessel <b>Characteristics</b></h2>
  <div class="title-rule"></div>
  <div class="vessel char" style="left:65px">
    <div class="vessel-art" style="width:64px" role="img" aria-label="Bulk carrier with cargo holds picture"></div>
    <div class="label"><h3>Holds and hatches<br>Draft</h3></div>
    <p>Omnis isasdte natus errorsit voluseptatem accusantium doloremque laudantium, totasem rsem.</p></div>
  <div class="vessel char" style="left:181px">
    <div class="vessel-art" style="width:78px" role="img" aria-label="Bulk carrier with deck cranes picture"></div>
    <div class="label"><h3>Beam</h3></div>
    <p>Omnis isasdte natus errorsit voluseptatem accusantium doloremque laudantium, totasem rsem.</p></div>
  <div class="vessel char" style="left:326px;width:160px;margin-left:-80px">
    <div class="vessel-art" style="width:94px" role="img" aria-label="Bulk carrier hatch covers picture"></div>
    <div class="label"><h3>Length Cargo Handling Equipment<br>Engine types</h3></div>
    <p>Omnis isasdte natus errorsit voluseptatem accusantium doloremque laudantium, totasem rsem.</p></div>
  <div class="vessel char" style="left:457px">
    <div class="vessel-art" style="width:86px" role="img" aria-label="Long bulk carrier side view picture"></div>
    <div class="label"><h3>Power</h3></div>
    <p>Omnis isasdte natus errorsit voluseptatem accusantium doloremque laudantium, totasem rsem.</p></div>
  <div class="footer"><span class="url"><i class="globe"><svg width="12" height="12"><use href="#i-globe"/></svg></i>www.bulkdeckbriefing.com</span>
    <span class="copy">© 2024. ALL Rights Reserved.</span><span class="page">Page<i>03</i></span></div>
</section>

<!-- Slide 4: routing -->
<section class="slide col-b row-2">
  <div class="brand heading">BULK <b>SHIPPING</b></div>
  <h2 class="slide-title heading">Routing in <b>Dry Bulk Shipping</b></h2>
  <div class="title-rule"></div>
  <div class="photo" style="left:38px;top:73px;width:223px;height:157px;background:linear-gradient(160deg,#2f6f9e 0%,#1d5583 55%,#234a6c 100%)" role="img" aria-label="Photo of a loaded container ship at sea"></div>
  <ul class="bullets" style="left:286px;top:88px;width:215px;font-size:12px;line-height:17.5px">
    <li>Major shipping routes (e.g., Cape of Good Hope, Panama Canal)</li>
    <li style="margin-top:18px">Factors influencing routing decisions (e.g., weather, fuel costs)</li>
    <li style="margin-top:18px">Strategic chokepoints and canals</li>
  </ul>
  <div class="footer"><span class="url"><i class="globe"><svg width="12" height="12"><use href="#i-globe"/></svg></i>www.bulkdeckbriefing.com</span>
    <span class="copy">© 2024. ALL Rights Reserved.</span><span class="page">Page<i>04</i></span></div>
</section>

<!-- Slide 5: chartering -->
<section class="slide col-a row-3">
  <div class="brand heading">BULK <b>SHIPPING</b></div>
  <h2 class="slide-title heading">Fixing and <b>Chartering</b></h2>
  <div class="title-rule"></div>
  <div class="photo" style="left:38px;top:73px;width:223px;height:157px;background:linear-gradient(150deg,#5f8fa0 0%,#2f6e78 50%,#1f5a5e 100%)" role="img" aria-label="Aerial photo of a container ship near the coast"></div>
  <ul class="bullets" style="left:286px;top:89px;line-height:18.5px">
    <li>Voyage Charter</li><li>Owner's responsibility</li><li>Charterer's responsibility</li>
    <li>Time Charter</li><li>Bareboat Charter</li><li>Spot and long-term contracts</li>
  </ul>
  <div class="footer"><span class="url"><i class="globe"><svg width="12" height="12"><use href="#i-globe"/></svg></i>www.bulkdeckbriefing.com</span>
    <span class="copy">© 2024. ALL Rights Reserved.</span><span class="page">Page<i>05</i></span></div>
</section>

<!-- Slide 6: CP terms -->
<section class="slide col-b row-3">
  <div class="brand heading">BULK <b>SHIPPING</b></div>
  <h2 class="slide-title heading">Key Charter Party <b>(CP) Terms</b></h2>
  <div class="title-rule"></div>
  <ul class="bullets" style="left:71px;top:113px;line-height:18.4px">
    <li>Laytime and demurrage</li><li>Freight rates</li><li>Notice of Readiness (NOR)</li>
    <li>Cargo quantities and quality</li><li>Ballast bonus</li>
  </ul>
  <div class="photo" style="left:238px;top:98px;width:222px;height:112px;background:linear-gradient(180deg,#eef0f2 0%,#c9ccd2 40%,#8d9199 75%,#d9c9ca 100%)" role="img" aria-label="Cut-out photo of a large container ship"></div>
  <div class="footer"><span class="url"><i class="globe"><svg width="12" height="12"><use href="#i-globe"/></svg></i>www.bulkdeckbriefing.com</span>
    <span class="copy">© 2024. ALL Rights Reserved.</span><span class="page">Page<i>06</i></span></div>
</section>

</body>
</html>
```